Poster/flyer design needed for Choral Concert

Please include the following text:<br/>Title of Event: Raise the Rafters!<br/>Subtitle: A Choral Festival of Song to celebrate Kinship Fortnight<br/>Kerrabee choirs come together to share their unique and beautiful music.<br/>Date: Sat March 21st 2020<br/>Time: 2pm - 4pm<br/>Venue: Tullaby Mechanics Hall<br/>Tickets: $10 each. Proceeds to Bushland Relief & TBF Crews<br/>Hosted By Lifted Tunes<br/>Featuring:<br/>Merrigal Unaccompanied Ladies' Chorus<br/>Wine of Dusk<br/>Kerrabee Neighbourhood Chorus<br/>Chant Together<br/>* design required for A4 poster and DL flyer (may be modified)<br/>* Please use orange as the main colour<br/>* The Kinship fortnight logo must be included (see attached - either is fine). The frame may be useful as well.<br/>* Please include musical images<br/>* Visit kinshipday.example.au for info on Kinship Fortnight

Target Market(s)

music-lovers, community-minded people, residents of the area, probably 30 + age

Industry/Entity Type

Entertainment

Font styles to use
Serif
Sans Serif

Colors
f78f20
ffffff

Requirements
Must have
• Orange colour
• Kinship logo
• required text
Nice to have
• A musical theme
Should not have
• writing should not be too small and difficult to read

```html
<!DOCTYPE html>
<html lang="en">
<head>
<meta charset="utf-8">
<title>Raise the Rafters! – Choral Festival Poster</title>
<link rel="stylesheet" href="https://fonts.googleapis.com/css2?family=Bitter:ital,wght@0,700;0,800;0,900;1,500;1,600&display=swap">
<style>
  :root {
    --stage: #f7f3cf;
    --ink-black: #000000;
    --deep-orange: #6a2a00;
    --orange: #f78f20;
    --orange-bright: #ffa534;
    --gold-light: #fff1b0;
    --gold: #f9c25a;
    --gold-deep: #e07a10;
    --text: #ffd98a;
    --white: #ffffff;
    --rule: #f78f20;
  }
  * { box-sizing: border-box; margin: 0; padding: 0; }
  html, body { width: 1200px; height: 800px; overflow: hidden; }
  body { background: var(--stage); position: relative; font-family: "Bitter", serif; }

  .poster {
    position: absolute; left: 334px; top: 24px; width: 532px; height: 752px;
    overflow: hidden; text-align: center;
    background:
      radial-gradient(ellipse 75% 40% at 50% 16%, #b85a0a 0%, var(--deep-orange) 45%, rgba(40,14,0,0.7) 75%, var(--ink-black) 100%),
      var(--ink-black);
    box-shadow: 0 4px 10px rgba(0,0,0,0.35);
  }
  .poster__decor {
    position: absolute; inset: 0; pointer-events: none;
    background:
      radial-gradient(ellipse 16% 42% at 3% 40%, rgba(247,143,32,0.8), transparent 70%),
      radial-gradient(ellipse 15% 48% at 97% 45%, rgba(247,143,32,0.85), transparent 70%),
      radial-gradient(ellipse 40% 14% at 30% 5%, rgba(255,200,110,0.3), transparent 70%),
      linear-gradient(to bottom, transparent 62%, rgba(0,0,0,0.85) 90%);
  }
  .content { position: relative; padding: 30px 40px 0; display: flex; flex-direction: column; align-items: center; }
  .gold {
    background: linear-gradient(180deg, var(--gold-light) 0%, var(--gold) 45%, var(--gold-deep) 100%);
    -webkit-background-clip: text; background-clip: text; color: transparent;
  }
  .title { display: flex; flex-direction: column; align-items: center; }
  .title-small { font-weight: 800; font-size: 42px; line-height: 44px; }
  .title-large { font-weight: 900; font-size: 80px; line-height: 82px; letter-spacing: -1px; }
  .subtitle {
    margin-top: 8px; width: 456px; padding: 4px 0 5px;
    background: rgba(255,255,255,0.1); border-radius: 8px;
    font-style: italic; font-weight: 600; font-size: 19px; line-height: 25px;
    letter-spacing: 1.5px; color: var(--text);
  }
  .intro { margin-top: 10px; font-style: italic; font-weight: 500; font-size: 15px; line-height: 20px; color: var(--white); width: 420px; }
  .block { margin-top: 12px; display: flex; flex-direction: column; align-items: center; }
  .label { font-weight: 800; font-size: 18px; letter-spacing: 1.5px; color: var(--orange-bright); line-height: 22px; padding: 0 8px 3px; border-bottom: 1px solid var(--rule); margin-bottom: 5px; }
  .detail { font-style: italic; font-weight: 600; color: var(--text); font-size: 19px; line-height: 23px; }
  .detail--sm { font-size: 16px; line-height: 21px; }
  .host { margin-top: 12px; font-weight: 700; font-size: 17px; color: var(--white); line-height: 22px; }
  .host strong { color: var(--orange-bright); font-weight: 700; }
  .brand {
    position: absolute; left: 0; right: 0; bottom: 10px;
    display: flex; justify-content: center; align-items: center; gap: 10px;
    font-weight: 800; font-size: 30px; line-height: 34px; color: var(--orange);
  }
  .brand__mark { width: 16px; height: 16px; background: var(--orange); }
</style>
</head>
<body>
  <main class="poster">
    <div class="poster__decor" role="img" aria-label="Flowing orange ribbons and arcs of glowing golden light"></div>

    <div class="content">
      <h1 class="title">
        <span class="title-small gold">Raise the</span>
        <span class="title-large gold">Rafters!</span>
      </h1>

      <p class="subtitle">A Choral Festival of Song to<br>celebrate Kinship Fortnight</p>

      <p class="intro">Kerrabee choirs come together to share their unique and beautiful music.</p>

      <section class="block">
        <h2 class="label">Date &amp; Time:</h2>
        <p class="detail">Sat March 21st 2020</p>
        <p class="detail">2pm - 4pm</p>
      </section>

      <section class="block">
        <h2 class="label">Venue:</h2>
        <p class="detail">Tullaby Mechanics Hall</p>
      </section>

      <section class="block">
        <h2 class="label">Tickets:</h2>
        <p class="detail detail--sm">$10 each.</p>
        <p class="detail detail--sm">Proceeds to Bushland Relief &amp; TBF Crews</p>
      </section>

      <p class="host">Hosted by <strong>Lifted Tunes</strong></p>

      <section class="block">
        <h2 class="label">Featuring:</h2>
        <p class="detail detail--sm">Merrigal Unaccompanied Ladies' Chorus</p>
        <p class="detail detail--sm">Wine of Dusk</p>
        <p class="detail detail--sm">Kerrabee Neighbourhood Chorus</p>
        <p class="detail detail--sm">Chant Together</p>
      </section>
    </div>

    <div class="brand"><span class="brand__mark"></span>Kinship Fortnight</div>
  </main>
</body>
</html>
```